Ferncliff Nutrients

Hi WP designers, this is my first time trying Pixel Guild ;-)

I would like a responsive woocommerce/wordpress theme for a company called Ferncliff nutrients. You can get an idea of what we sell, and how bad our old site is here:http://www.ferncliffnutrients-example.com.sg/

Would love to see any type of modern looking design, a few guidelines:
- We've got a logo (see attached)
- We like green as a base for the colour scheme to match the logo but open to ideas

Target Market(s)

90% of customers will be Singaporean looking for good deals on top brands they already buy.

Industry/Entity Type

It Company

Font styles to use
Other font styles liked:
• Open Sans

Colors
9bcb3c
add136
cadf82
0492cd
eb1f27
a6459a
f78f20
ffc214

Requirements
Must have
• Sign In/Sign UpNewsletter sign up: best dealsFeatured deals sectionRatings/Reviews on products
Nice to have
• We're open to any ideas but would perhaps like to see something minimalist and easy on the eyes.
• Try to keep mostly images and white space
Should not have
• Too much text

```html
<!DOCTYPE html>
<html lang="en">
<head>
<meta charset="utf-8">
<title>Ferncliff Nutrients – Store</title>
<link href="https://fonts.googleapis.com/css2?family=Open+Sans:wght@300;400;600;700&family=Roboto+Slab:wght@400&display=swap" rel="stylesheet">
<style>
:root{
  --green:#4b5f33;
  --page:#f3f3f3;
  --header:#f8f8f8;
  --nav:#e7e7e7;
  --text:#555;
  --text-dark:#444;
  --heading:#4a4a4a;
  --star:#e2bd1c;
  --star-off:#b5b5b5;
  --footer:#cfcdcd;
  --footer-line:#bdbbbb;
  --bottom:#ebebeb;
  --herb-light:#c9dc7a;
  --herb:#7fa23a;
  --herb-deep:#4f6f22;
  --omega:#b4d65a;
  --vitc:#eab68a;
}
*{box-sizing:border-box;margin:0;padding:0}
html,body{width:856px;height:1200px;overflow:hidden}
body{font-family:"Open Sans",Arial,sans-serif;color:var(--text);background:var(--page);font-size:10px}
.page{position:relative;width:856px;height:1200px;overflow:hidden;background:var(--page)}
.abs{position:absolute}
.btn{display:flex;align-items:center;justify-content:center;border:1px solid #ccc;border-radius:2px;background:linear-gradient(#fff,#ececec);color:var(--text-dark);font-size:9px}

/* header */
.site-header{left:0;top:0;width:856px;height:82px;background:var(--header);border-bottom:1px solid #e2e2e2}
.brand{left:100px;top:40px;display:flex;align-items:center;gap:6px;font-size:14px;font-weight:400;color:#333;letter-spacing:.3px;text-transform:uppercase}
.brand-mark{width:11px;height:11px;background:#333}
.tool{top:19px;height:21px}
.search{left:633px;top:19px;width:98px;height:21px;border:1px solid #ccc;background:#fff;font-size:8px;color:#999;padding:5px 6px;border-radius:2px 0 0 2px}
.search-btn{left:731px;top:19px;width:25px;height:21px;background:var(--green);border-radius:0 2px 2px 0;display:flex;align-items:center;justify-content:center}

/* nav */
.main-nav{left:0;top:82px;width:856px;height:29px;background:var(--nav);border-bottom:1px solid #d8d8d8;border-top:1px solid #dcdcdc}
.nav-item{top:0;height:28px;border-right:1px solid #d0d0d0;display:flex;align-items:center;justify-content:center;gap:5px;font-size:9px;color:#444;letter-spacing:.3px}
.nav-home{left:93px;width:37px;background:var(--green);border:none}
.caret{width:0;height:0;border-left:3px solid transparent;border-right:3px solid transparent;border-top:3px solid #444}

/* slider */
.hero{left:93px;top:155px;width:437px;height:217px;border:3px solid #fff;box-shadow:0 1px 3px rgba(0,0,0,.25);
  background:
    radial-gradient(ellipse 60% 45% at 30% 85%,rgba(246,236,170,.85),rgba(246,236,170,0) 70%),
    radial-gradient(ellipse 45% 40% at 62% 45%,rgba(238,238,232,.9),rgba(238,238,232,0) 70%),
    linear-gradient(180deg,var(--herb-light) 0%,var(--herb) 28%,var(--herb-deep) 55%,var(--herb) 80%,var(--herb-light) 100%)}
.pager{top:362px;display:flex;gap:3px;left:297px}
.dot{width:16px;height:16px;border-radius:50%;display:flex;align-items:center;justify-content:center;font-size:8px;font-weight:700}
.dot.on{background:#444;color:#fff}
.dot.off{background:#fff;color:#444;border:1.5px solid #444}

/* section heading */
.section-head{display:flex;align-items:center;height:16px}
.section-title{font-family:"Roboto Slab",Georgia,serif;font-size:10px;color:var(--heading);letter-spacing:.4px;white-space:nowrap;padding-right:8px}
.section-rule{flex:1;border-top:1px dotted #bbb}
.view-all{height:15px;padding:0 5px;margin-left:6px}

/* special */
.special{left:544px;top:154px;width:212px}
.arrow-btn{width:13px;height:13px;margin-left:2px}
.special-item{left:544px;width:212px;height:72px}
.thumb{left:0;top:0;width:72px;height:72px;border:1px solid #ddd;box-shadow:0 1px 2px rgba(0,0,0,.1);
  background:radial-gradient(ellipse 30% 42% at 50% 50%,#e4e7dc,#f3f3ef 70%,#fff 100%)}
.special-name{left:76px;top:0;width:120px;font-size:8.5px;font-weight:600;color:#555;line-height:14px}
.special-rule{left:76px;width:136px;border-top:1px solid #ddd}
.special-price{left:76px;font-size:10px;font-weight:600;color:#444}
.special-stars{left:76px}

/* featured */
.featured{left:93px;top:423px;width:663px}
.grid{left:93px;width:664px;display:flex;gap:15px}
.product{width:155px;position:relative;height:210px}
.product-img{position:absolute;left:0;top:0;width:155px;height:140px;border:1px solid #ddd;box-shadow:0 1px 3px rgba(0,0,0,.12)}
.product-img.omega{background:radial-gradient(ellipse 26% 42% at 50% 55%,var(--omega),#dbe9b5 60%,#fff 100%)}
.product-img.vitc{background:radial-gradient(ellipse 26% 42% at 50% 55%,var(--vitc),#f3dcc6 60%,#fff 100%)}
.product-name{position:absolute;left:0;top:146px;width:155px;font-size:8.5px;font-weight:600;line-height:14px;color:#555}
.product-price{position:absolute;left:0;top:176px;width:155px;height:18px;font-size:10.5px;font-weight:600;color:#444;border-bottom:1px dotted #bbb}
.product-actions{position:absolute;left:0;top:200px;width:155px;display:flex;align-items:center;gap:3px}
.act{width:25px;height:18px}
.act.cart{background:var(--green);border-color:var(--green)}
.product-actions .stars{margin-left:auto}
.stars{display:flex;gap:1px}

/* footer */
.site-footer{left:0;top:1007px;width:856px;height:154px;background:var(--footer)}
.footer-title{font-family:"Roboto Slab",Georgia,serif;font-size:10px;color:#444;letter-spacing:.4px;display:inline-block;padding:0 4px 2px 0;border-bottom:1px solid #444}
.col-head{top:1021px;border-bottom:1px solid var(--footer-line);height:18px}
.links{top:1047px;list-style:none;width:158px}
.links li{height:23px;border-bottom:1px solid var(--footer-line);display:flex;align-items:center;gap:7px;font-size:8.5px;color:#555}
.links li:last-child{border-bottom:none}
.tri{width:0;height:0;border-top:3.5px solid transparent;border-bottom:3.5px solid transparent;border-left:4px solid #555}
.contact{left:431px;top:1045px;width:156px;list-style:none}
.contact li{height:32px;display:flex;align-items:center;gap:9px;font-size:8.5px;font-weight:600;color:#555;border-bottom:1px solid var(--footer-line)}
.contact li:last-child{border-bottom:none}
.ic{width:20px;height:20px;border-radius:50%;background:#f2f2f2;display:flex;align-items:center;justify-content:center}
.field{left:601px;width:155px;height:20px;background:#fff;border:1px solid #ccc;border-radius:2px;font-size:7.5px;color:#999;padding:5px 5px}
.join{left:601px;top:1110px;width:155px;height:20px;font-size:8.5px}
.bottom-bar{left:0;top:1161px;width:856px;height:39px;background:var(--bottom)}
.copy{left:93px;top:1173px;font-size:8.5px;color:#555}
.cards{left:615px;top:1170px;display:flex;gap:6px}
.card{width:26px;height:18px;border-radius:2px;border:1px solid #bbb}
</style>
</head>
<body>
<svg width="0" height="0" style="position:absolute">
  <defs>
    <symbol id="star" viewBox="0 0 20 20"><path d="M10 1l2.6 5.8 6.3.6-4.8 4.2 1.4 6.2L10 14.6 4.5 17.8l1.4-6.2L1.1 7.4l6.3-.6z"/></symbol>
    <symbol id="cart" viewBox="0 0 20 20"><path d="M2 3h3l2 9h9l2-6H6" fill="none" stroke="currentColor" stroke-width="2"/><circle cx="8" cy="16" r="1.6"/><circle cx="15" cy="16" r="1.6"/></symbol>
    <symbol id="heart" viewBox="0 0 20 20"><path d="M10 17L3 10a4 4 0 016-5l1 1 1-1a4 4 0 016 5z"/></symbol>
    <symbol id="swap" viewBox="0 0 20 20"><path d="M15 8a5.5 5.5 0 00-10-1M5 12a5.5 5.5 0 0010 1" fill="none" stroke="currentColor" stroke-width="1.8"/><path d="M3 4v4h4zM17 16v-4h-4z"/></symbol>
  </defs>
</svg>

<div class="page">

  <header class="site-header abs">
    <div class="brand abs"><span class="brand-mark"></span>Ferncliff Nutrients</div>
    <div class="btn tool abs" style="left:480px;width:31px">$ &#9662;</div>
    <div class="btn tool abs" style="left:517px;width:38px">EN &#9662;</div>
    <div class="btn tool abs" style="left:561px;width:65px;gap:3px">
      <svg width="9" height="9" fill="#444" color="#444"><use href="#cart"/></svg>3 Items &#9662;
    </div>
    <div class="search abs">Search...</div>
    <div class="search-btn abs">
      <svg width="9" height="9" viewBox="0 0 10 10"><circle cx="4" cy="4" r="3" fill="none" stroke="#fff" stroke-width="1.5"/><path d="M6.3 6.3L9 9" stroke="#fff" stroke-width="1.6"/></svg>
    </div>
  </header>

  <nav class="main-nav abs">
    <div class="nav-item nav-home abs">
      <svg width="11" height="10" viewBox="0 0 12 10"><path d="M6 0L0 5h1.5v5h3V7h3v3h3V5H12z" fill="#fff"/></svg>
    </div>
    <div class="nav-item abs" style="left:130px;width:69px">ABOUT US</div>
    <div class="nav-item abs" style="left:199px;width:84px">PRODUCTS <span class="caret"></span></div>
    <div class="nav-item abs" style="left:283px;width:65px">SHOP <span class="caret"></span></div>
    <div class="nav-item abs" style="left:348px;width:65px">CONTACT</div>
  </nav>

  <div class="hero abs" role="img" aria-label="Slide photo: fresh green herbs, white mortar and pestle and yellow flowers"></div>
  <div class="pager abs"><span class="dot on">1</span><span class="dot off">2</span></div>

  <section class="special abs">
    <div class="section-head">
      <span class="section-title">SPECIAL</span><span class="section-rule"></span>
      <span class="btn arrow-btn">&#9662;</span><span class="btn arrow-btn">&#9652;</span>
      <span class="btn view-all">View All</span>
    </div>
  </section>

  <div class="special-item abs" style="top:194px">
    <div class="thumb abs" role="img" aria-label="Product photo: white supplement bottle"></div>
    <div class="special-name abs">Leafworks the title here</div>
    <div class="special-rule abs" style="top:18px"></div>
    <div class="special-price abs" style="top:22px">$150.00</div>
    <div class="special-stars stars abs" style="top:42px">
      <svg width="12" height="12" fill="var(--star-off)"><use href="#star"/></svg><svg width="12" height="12" fill="var(--star-off)"><use href="#star"/></svg><svg width="12" height="12" fill="var(--star-off)"><use href="#star"/></svg><svg width="12" height="12" fill="var(--star-off)"><use href="#star"/></svg><svg width="12" height="12" fill="var(--star-off)"><use href="#star"/></svg>
    </div>
  </div>

  <div class="special-item abs" style="top:293px">
    <div class="thumb abs" role="img" aria-label="Product photo: white supplement bottle"></div>
    <div class="special-name abs">Leafworks the designer portfolio</div>
    <div class="special-price abs" style="top:34px">$150.00</div>
    <div class="special-rule abs" style="top:32px"></div>
    <div class="special-stars stars abs" style="top:54px">
      <svg width="12" height="12" fill="var(--star)"><use href="#star"/></svg><svg width="12" height="12" fill="var(--star)"><use href="#star"/></svg><svg width="12" height="12" fill="var(--star)"><use href="#star"/></svg><svg width="12" height="12" fill="var(--star-off)"><use href="#star"/></svg><svg width="12" height="12" fill="var(--star-off)"><use href="#star"/></svg>
    </div>
  </div>

  <section class="featured abs">
    <div class="section-head">
      <span class="section-title">FEATURED ITEMS</span><span class="section-rule"></span>
      <span class="btn view-all">View All</span>
    </div>
  </section>

  <div class="grid abs" style="top:466px">
    <article class="product">
      <div class="product-img omega" role="img" aria-label="Product photo: green Omegas 3-6 supplement tub"></div>
      <div class="product-name">Leafworks the designer portfolio brochure</div>
      <div class="product-price">$150.00</div>
      <div class="product-actions">
        <span class="btn act cart"><svg width="10" height="10" fill="#fff" color="#fff"><use href="#cart"/></svg></span>
        <span class="btn act"><svg width="9" height="9" fill="#444"><use href="#heart"/></svg></span>
        <span class="btn act"><svg width="9" height="9" fill="#444" color="#444"><use href="#swap"/></svg></span>
        <span class="stars"><svg width="11" height="11" fill="var(--star)"><use href="#star"/></svg><svg width="11" height="11" fill="var(--star)"><use href="#star"/></svg><svg width="11" height="11" fill="var(--star)"><use href="#star"/></svg><svg width="11" height="11" fill="var(--star)"><use href="#star"/></svg><svg width="11" height="11" fill="var(--star-off)"><use href="#star"/></svg></span>
      </div>
    </article>
    <article class="product">
      <div class="product-img vitc" role="img" aria-label="Product photo: orange Vitamin C supplement tub"></div>
      <div class="product-name">Leafworks the designer portfolio brochure</div>
      <div class="product-price">$150.00</div>
      <div class="product-actions">
        <span class="btn act cart"><svg width="10" height="10" fill="#fff" color="#fff"><use href="#cart"/></svg></span>
        <span class="btn act"><svg width="9" height="9" fill="#444"><use href="#heart"/></svg></span>
        <span class="btn act"><svg width="9" height="9" fill="#444" color="#444"><use href="#swap"/></svg></span>
        <span class="stars"><svg width="11" height="11" fill="var(--star)"><use href="#star"/></svg><svg width="11" height="11" fill="var(--star)"><use href="#star"/></svg><svg width="11" height="11" fill="var(--star)"><use href="#star"/></svg><svg width="11" height="11" fill="var(--star-off)"><use href="#star"/></svg><svg width="11" height="11" fill="var(--star-off)"><use href="#star"/></svg></span>
      </div>
    </article>
    <article class="product">
      <div class="product-img vitc" role="img" aria-label="Product photo: orange Vitamin C supplement tub"></div>
      <div class="product-name">Leafworks the designer portfolio brochure</div>
      <div class="product-price">$150.00</div>
      <div class="product-actions">
        <span class="btn act cart"><svg width="10" height="10" fill="#fff" color="#fff"><use href="#cart"/></svg></span>
        <span class="btn act"><svg width="9" height="9" fill="#444"><use href="#heart"/></svg></span>
        <span class="btn act"><svg width="9" height="9" fill="#444" color="#444"><use href="#swap"/></svg></span>
        <span class="stars"><svg width="11" height="11" fill="var(--star)"><use href="#star"/></svg><svg width="11" height="11" fill="var(--star)"><use href="#star"/></svg><svg width="11" height="11" fill="var(--star)"><use href="#star"/></svg><svg width="11" height="11" fill="var(--star-off)"><use href="#star"/></svg><svg width="11" height="11" fill="var(--star-off)"><use href="#star"/></svg></span>
      </div>
    </article>
    <article class="product">
      <div class="product-img omega" role="img" aria-label="Product photo: green Omegas 3-6 supplement tub"></div>
      <div class="product-name">Leafworks the designer portfolio brochure</div>
      <div class="product-price">$150.00</div>
      <div class="product-actions">
        <span class="btn act cart"><svg width="10" height="10" fill="#fff" color="#fff"><use href="#cart"/></svg></span>
        <span class="btn act"><svg width="9" height="9" fill="#444"><use href="#heart"/></svg></span>
        <span class="btn act"><svg width="9" height="9" fill="#444" color="#444"><use href="#swap"/></svg></span>
        <span class="stars"><svg width="11" height="11" fill="var(--star)"><use href="#star"/></svg><svg width="11" height="11" fill="var(--star)"><use href="#star"/></svg><svg width="11" height="11" fill="var(--star)"><use href="#star"/></svg><svg width="11" height="11" fill="var(--star-off)"><use href="#star"/></svg><svg width="11" height="11" fill="var(--star-off)"><use href="#star"/></svg></span>
      </div>
    </article>
  </div>

  <div class="grid abs" style="top:720px">
    <article class="product">
      <div class="product-img vitc" role="img" aria-label="Product photo: orange Vitamin C supplement tub"></div>
      <div class="product-name">Leafworks the designer portfolio brochure</div>
      <div class="product-price">$150.00</div>
      <div class="product-actions">
        <span class="btn act cart"><svg width="10" height="10" fill="#fff" color="#fff"><use href="#cart"/></svg></span>
        <span class="btn act"><svg width="9" height="9" fill="#444"><use href="#heart"/></svg></span>
        <span class="btn act"><svg width="9" height="9" fill="#444" color="#444"><use href="#swap"/></svg></span>
        <span class="stars"><svg width="11" height="11" fill="var(--star)"><use href="#star"/></svg><svg width="11" height="11" fill="var(--star)"><use href="#star"/></svg><svg width="11" height="11" fill="var(--star)"><use href="#star"/></svg><svg width="11" height="11" fill="var(--star-off)"><use href="#star"/></svg><svg width="11" height="11" fill="var(--star-off)"><use href="#star"/></svg></span>
      </div>
    </article>
    <article class="product">
      <div class="product-img omega" role="img" aria-label="Product photo: green Omegas 3-6 supplement tub"></div>
      <div class="product-name">Leafworks the designer portfolio brochure</div>
      <div class="product-price">$150.00</div>
      <div class="product-actions">
        <span class="btn act cart"><svg width="10" height="10" fill="#fff" color="#fff"><use href="#cart"/></svg></span>
        <span class="btn act"><svg width="9" height="9" fill="#444"><use href="#heart"/></svg></span>
        <span class="btn act"><svg width="9" height="9" fill="#444" color="#444"><use href="#swap"/></svg></span>
        <span class="stars"><svg width="11" height="11" fill="var(--star)"><use href="#star"/></svg><svg width="11" height="11" fill="var(--star)"><use href="#star"/></svg><svg width="11" height="11" fill="var(--star)"><use href="#star"/></svg><svg width="11" height="11" fill="var(--star-off)"><use href="#star"/></svg><svg width="11" height="11" fill="var(--star-off)"><use href="#star"/></svg></span>
      </div>
    </article>
    <article class="product">
      <div class="product-img vitc" role="img" aria-label="Product photo: orange Vitamin C supplement tub"></div>
      <div class="product-name">Leafworks the designer portfolio brochure</div>
      <div class="product-price">$150.00</div>
      <div class="product-actions">
        <span class="btn act cart"><svg width="10" height="10" fill="#fff" color="#fff"><use href="#cart"/></svg></span>
        <span class="btn act"><svg width="9" height="9" fill="#444"><use href="#heart"/></svg></span>
        <span class="btn act"><svg width="9" height="9" fill="#444" color="#444"><use href="#swap"/></svg></span>
        <span class="stars"><svg width="11" height="11" fill="var(--star)"><use href="#star"/></svg><svg width="11" height="11" fill="var(--star)"><use href="#star"/></svg><svg width="11" height="11" fill="var(--star)"><use href="#star"/></svg><svg width="11" height="11" fill="var(--star-off)"><use href="#star"/></svg><svg width="11" height="11" fill="var(--star-off)"><use href="#star"/></svg></span>
      </div>
    </article>
    <article class="product">
      <div class="product-img vitc" role="img" aria-label="Product photo: orange Vitamin C supplement tub"></div>
      <div class="product-name">Leafworks the designer portfolio brochure</div>
      <div class="product-price">$150.00</div>
      <div class="product-actions">
        <span class="btn act cart"><svg width="10" height="10" fill="#fff" color="#fff"><use href="#cart"/></svg></span>
        <span class="btn act"><svg width="9" height="9" fill="#444"><use href="#heart"/></svg></span>
        <span class="btn act"><svg width="9" height="9" fill="#444" color="#444"><use href="#swap"/></svg></span>
        <span class="stars"><svg width="11" height="11" fill="var(--star)"><use href="#star"/></svg><svg width="11" height="11" fill="var(--star)"><use href="#star"/></svg><svg width="11" height="11" fill="var(--star)"><use href="#star"/></svg><svg width="11" height="11" fill="var(--star-off)"><use href="#star"/></svg><svg width="11" height="11" fill="var(--star-off)"><use href="#star"/></svg></span>
      </div>
    </article>
  </div>

  <footer class="site-footer abs"></footer>

  <div class="col-head abs" style="left:93px;width:330px"><span class="footer-title">USEFULL LINKS</span></div>
  <ul class="links abs" style="left:97px">
    <li><span class="tri"></span>About Us</li>
    <li><span class="tri"></span>Delivery Information</li>
    <li><span class="tri"></span>Privacy Police</li>
    <li><span class="tri"></span>Terms &amp; Conditions</li>
  </ul>
  <ul class="links abs" style="left:262px">
    <li><span class="tri"></span>Surf Brands</li>
    <li><span class="tri"></span>Site Map</li>
  </ul>

  <div class="col-head abs" style="left:431px;width:156px"><span class="footer-title">CONTACT INFO</span></div>
  <ul class="contact abs">
    <li><span class="ic"><svg width="11" height="10" viewBox="0 0 12 10"><path d="M1 3h3l4-3v10L4 7H1z" fill="#444"/><path d="M9.5 3a3 3 0 010 4" fill="none" stroke="#444"/></svg></span>Call Us: 555-010-2030</li>
    <li><span class="ic"><svg width="11" height="9" viewBox="0 0 12 9"><rect width="12" height="9" rx="1" fill="#444"/><path d="M0.5 1l5.5 4 5.5-4" fill="none" stroke="#f2f2f2"/></svg></span>hello@ferncliff-example.com</li>
    <li><span class="ic"><svg width="8" height="11" viewBox="0 0 8 11"><path d="M4 11S0 6.5 0 4a4 4 0 018 0c0 2.5-4 7-4 7z" fill="#444"/><circle cx="4" cy="4" r="1.5" fill="#f2f2f2"/></svg></span>Greenvale, Sunny Park</li>
  </ul>

  <div class="col-head abs" style="left:601px;width:155px"><span class="footer-title">NEWSLETTER</span></div>
  <div class="field abs" style="top:1054px">Your Name...</div>
  <div class="field abs" style="top:1082px">Your E-Mail...</div>
  <div class="btn join abs">Join Us Now</div>

  <div class="bottom-bar abs"></div>
  <div class="copy abs">© Copyrights 2014</div>
  <div class="cards abs" aria-label="Accepted payment cards">
    <span class="card" style="background:#e9eef7"></span>
    <span class="card" style="background:#eef2f8"></span>
    <span class="card" style="background:#2a5aa3"></span>
    <span class="card" style="background:#f1ece4"></span>
  </div>

</div>
</body>
</html>
```